Business card for Industrial Automation Company.

The company is called Process and Signal Dynamics. We are a systems integration company in South Africa specializing in PLC and SCADA programming, systems integration and industrial automation. Attached find logo and cover letter of the company for a feel of the general look. The website is still under development, so you will have to use your own ideas.

Please blend the colors on the business card as per the logo colors. Must be clean, professional look. Please submit a creative professional design. If a background color is used please do not use dark colored backgrounds.

Target Market(s)

Mining

Industry/Entity Type

Engineering Consultant

Contact Information for Business Card

Gerrit van Dyk (NDip Electrical LC; BSc)
Director / Systems Engineer

Postal Address
PO Box 2867
Vredenburg
7380

Physical Address:
Kloofhoek Street 27
Vredenburg
7380

Tel: +22 548 6170
Cell: +27 82 953 4086
Mail: gerritv@psd-zx.com
Web: www.psd-zx.com

Font styles to use
Sans Serif

Colors

Designer to choose colors to be used in the design.

Requirements
Must have
• Backside of the card must also contain the following:
• Services
• *Industrial Automation
• *Control System design and configuration
• *Systems Integration
• *Equipment Supply
• Industries
• *Mining
• *Factory
• *Oil and Gas
Nice to have
• Colors must blend in with colors of logo. Not too much color and no dark backgrounds.
Should not have
• dark / black background. Preferably white / light background if any.

```html
<!DOCTYPE html>
<html lang="en">
<head>
<meta charset="utf-8">
<title>Process and Signal Dynamics – Business Card</title>
<link href="https://fonts.googleapis.com/css2?family=Source+Sans+3:wght@400;600;700&display=swap" rel="stylesheet">
<style>
  :root {
    --stage: #232323;
    --brand-blue: #1a4a80;
    --brand-lime: #d6e128;
    --paper: #ffffff;
    --ink-grey: #555a60;
    --on-blue: #ffffff;
  }
  * { margin: 0; padding: 0; box-sizing: border-box; }
  html, body { width: 1200px; height: 900px; overflow: hidden; }
  body {
    background: var(--stage);
    font-family: "Source Sans 3", Arial, sans-serif;
    position: relative;
  }
  .card {
    position: absolute;
    left: 319px;
    width: 584px;
    height: 359px;
    overflow: hidden;
    box-shadow: 2px 3px 6px rgba(0,0,0,0.6);
  }
  .card--front { top: 87px; background: var(--brand-lime); }
  .card--back { top: 477px; height: 360px; background: var(--paper); }
  .card__backdrop { position: absolute; inset: 0; }
  .abs { position: absolute; line-height: 1; white-space: nowrap; }

  /* brand lockup */
  .brand { display: flex; align-items: center; gap: 12px; }
  .brand__dot { width: 22px; height: 22px; border-radius: 50%; flex: none; }
  .brand__name { font-weight: 700; font-size: 27px; letter-spacing: -0.2px; }
  .brand__tagline { font-size: 17px; letter-spacing: 0.6px; }
  .card--front .brand__dot { background: var(--brand-lime); }
  .card--front .brand__name,
  .card--front .brand__tagline { color: var(--on-blue); }
  .card--back .brand__dot { background: var(--brand-blue); }
  .card--back .brand__name { color: var(--brand-blue); }
  .card--back .brand__tagline { color: var(--ink-grey); }

  /* front contact */
  .person__name { font-weight: 600; font-size: 18px; color: var(--on-blue); }
  .person__role { font-size: 16px; color: var(--on-blue); }
  .contact-list { list-style: none; }
  .contact-list li {
    display: flex; align-items: center; gap: 7px;
    font-size: 15.5px; color: var(--on-blue); height: 21px;
  }
  .contact-list svg { width: 13px; height: 13px; fill: var(--on-blue); flex: none; }
  .address { text-align: right; right: 33px; color: var(--on-blue); }
  .address__title { font-weight: 600; font-size: 18px; margin-bottom: 5px; }
  .address__line { font-size: 16px; line-height: 21px; }

  /* back lists */
  .section-title { font-weight: 600; font-size: 20px; color: var(--brand-blue); }
  .bullet-list { list-style: none; }
  .bullet-list li {
    font-size: 16px; color: var(--ink-grey); height: 21px;
    display: flex; align-items: center; gap: 7px;
  }
  .bullet-list li::before {
    content: ""; width: 7px; height: 7px; border-radius: 50%;
    background: var(--brand-blue); flex: none;
  }
</style>
</head>
<body>

<section class="card card--front" aria-label="Business card front">
  <svg class="card__backdrop" width="584" height="359" viewBox="0 0 584 359" aria-hidden="true">
    <path d="M0 62 C160 10 330 20 450 70 C520 100 560 130 584 145 L584 359 L0 359 Z" fill="#1a4a80"/>
  </svg>

  <div class="abs brand" style="left:37px; top:100px;">
    <span class="brand__dot"></span>
    <span class="brand__name">Process and Signal Dynamics</span>
  </div>
  <div class="abs brand__tagline" style="left:131px; top:141px;">Partnering for innovative solutions!</div>

  <div class="abs person__name" style="left:37px; top:183px;">Gerrit van Dyk (NDip Electrical LC; BSc)</div>
  <div class="abs person__role" style="left:37px; top:206px;">Director / Systems Engineer</div>

  <ul class="abs contact-list" style="left:37px; top:236px;">
    <li><svg viewBox="0 0 16 16"><path d="M1 6c0-3 3-4 7-4s7 1 7 4l-3 1-1-2H5L4 7 1 6zm3 2h8l2 6H2z"/></svg>+22 548 6170</li>
    <li><svg viewBox="0 0 16 16"><path d="M4 0h8v16H4zM5.5 2v10h5V2zM7 13.5h2v1H7z" fill-rule="evenodd"/></svg>+27 82 953 4086</li>
    <li><svg viewBox="0 0 16 16"><path d="M1 3h14v10H1zM2 4.5v.5l6 4 6-4v-.5z" fill-rule="evenodd"/></svg>gerritv@psd-zx.com</li>
    <li><svg viewBox="0 0 16 16"><circle cx="8" cy="8" r="7"/><path d="M5 4l3 2-1 3 2 3 2-4-2-2 1-2" fill="#1a4a80"/></svg>www.psd-zx.com</li>
  </ul>

  <div class="abs address" style="top:187px;">
    <div class="address__title">Postal Address</div>
    <div class="address__line">PO Box 2867</div>
    <div class="address__line">Vredenburg 7380</div>
  </div>
  <div class="abs address" style="top:261px;">
    <div class="address__title">Physical Address</div>
    <div class="address__line">Kloofhoek Street 27</div>
    <div class="address__line">Vredenburg 7380</div>
  </div>
</section>

<section class="card card--back" aria-label="Business card back">
  <div class="abs brand" style="left:37px; top:42px;">
    <span class="brand__dot"></span>
    <span class="brand__name">Process and Signal Dynamics</span>
  </div>
  <div class="abs brand__tagline" style="left:142px; top:102px;">Partnering for innovative solutions!</div>

  <h2 class="abs section-title" style="left:37px; top:140px;">SERVICES</h2>
  <ul class="abs bullet-list" style="left:37px; top:174px;">
    <li>Industrial Automation</li>
    <li>Control System design and configuration</li>
    <li>Systems Integration</li>
    <li>Equipment Supply</li>
  </ul>

  <h2 class="abs section-title" style="left:37px; top:278px;">INDUSTRIES</h2>
  <ul class="abs bullet-list" style="left:37px; top:307px;">
    <li>&nbsp;Mining | Factory | Oil and Gas</li>
  </ul>
</section>

</body>
</html>
```